Etikett für Flaschenwein gesucht
Zielgruppe
Weingeschäft -> Verkauf von Flaschenweine; Zielgruppe: Weintrinker, Genusstrinker oder auch jene Personen, die beim Einkaufen einfach gerne eine Flasche Wein mitnehmen wollen und bewusst unsere Weinflasche wählen, da ihnen das Design der Etikette zusagt; !!! Folgeaufträge denkbar!!! für Weinkarten Design, Roll-Up, Autobeschriftungen u.v.m
Aufgabenstellung
Schlicht, elegant und modern; Entwurf einer Weinetikette für exclusive Weine, ev. auch mit dem Namen des Weinguts -> 'Fenzl' eine Marke/ein Logo gestalten bzw. soll auf der Etikette auf alle Fälle Name des Betriebs u. auch die Sorte z.b. 'Weinviertel DAC' ersichtlich sein.
Es gibt momentan Etiketten u. ein Logo aber auf Grund des Betriebsführer-Wechsels (alte Generation übergibt an die neue Generation) kann man hier unvoreingenommen kreativ sein, daher auch kein Upload von bestehenden Dateien.

```html
<!DOCTYPE html>
<html lang="de">
<head>
<meta charset="utf-8">
<title>Fenzl – Weinviertel DAC Etikett</title>
<link href="https://fonts.googleapis.com/css2?family=Montserrat:wght@300;500&family=Fira+Sans:wght@400&display=swap" rel="stylesheet">
<style>
  :root {
    --paper: #ffffff;
    --ink: #000000;
    --copper: #c0916a;
    --panel: #e8e8e8;
    --vine: #8b7d60;
  }
  html, body {
    margin: 0;
    padding: 0;
    overflow: hidden;
    background: var(--paper);
  }
  .label {
    position: relative;
    width: 878px;
    height: 1200px;
    background: var(--paper);
    box-sizing: border-box;
    border: 3px solid var(--ink);
    overflow: hidden;
  }
  .inner-frame {
    position: absolute;
    left: 189px;
    top: 143px;
    width: 499px;
    height: 914px;
    box-sizing: border-box;
    border: 3px solid var(--ink);
  }
  .brand {
    position: absolute;
    left: 294px;
    top: 297px;
    margin: 0;
    font-family: "Montserrat", sans-serif;
    font-weight: 500;
    font-size: 150px;
    line-height: 138px;
    letter-spacing: 0.02em;
    color: var(--copper);
    white-space: nowrap;
  }
  .brand span { display: block; }
  .variety-box {
    position: absolute;
    left: 284px;
    top: 570px;
    width: 309px;
    height: 272px;
    box-sizing: border-box;
    border: 4px solid var(--ink);
    padding: 5px;
  }
  .variety-inner {
    width: 100%;
    height: 100%;
    box-sizing: border-box;
    border: 3px solid var(--ink);
    background: var(--panel);
  }
  .variety {
    position: absolute;
    left: 321px;
    top: 602px;
    margin: 0;
    font-family: "Montserrat", sans-serif;
    font-weight: 300;
    font-size: 55px;
    line-height: 66px;
    color: var(--ink);
  }
  .variety span { display: block; }
  .vine-art {
    position: absolute;
    left: 0;
    top: 690px;
    width: 440px;
    height: 510px;
  }
  .description {
    position: absolute;
    left: 239px;
    top: 1061px;
    width: 440px;
    margin: 0;
    font-family: "Fira Sans", sans-serif;
    font-size: 23px;
    line-height: 35px;
    letter-spacing: 0.01em;
    text-align: center;
    color: var(--ink);
    white-space: nowrap;
  }
</style>
</head>
<body>
  <main class="label">
    <div class="inner-frame"></div>

    <h1 class="brand"><span>FEN</span><span>ZL</span></h1>

    <div class="variety-box"><div class="variety-inner"></div></div>
    <p class="variety"><span>WEIN</span><span>VIERTEL</span><span>DAC</span></p>

    <svg class="vine-art" viewBox="0 0 440 510" role="img" aria-label="Handgezeichnete Weintraube mit Weinblättern in Olivbraun">
      <defs>
        <radialGradient id="vineTone" cx="50%" cy="50%" r="50%">
          <stop offset="0%" stop-color="#8b7d60" stop-opacity="0.3"/>
          <stop offset="60%" stop-color="#8b7d60" stop-opacity="0.12"/>
          <stop offset="100%" stop-color="#8b7d60" stop-opacity="0"/>
        </radialGradient>
      </defs>
      <rect width="440" height="510" fill="url(#vineTone)"/>
    </svg>

    <p class="description">FenzlLorem ipsum dolor sit<br>amet, consectetuer adipiscing elit,<br>sed diam</p>
  </main>
</body>
</html>
```